Quorenta - Automated robotic Inspection with AI need new business cards

We need a new design of our business cards. The company is focused on automated quality control at high speed with unmatched results. We have a logo but need a more forward leaning business card that shows that we are delivering cutting edge technology.

Contact Information for Business Card

Name
Position
Adress
Phone
Email
e.g.
Lotta Berglund
Chief Financial Officer (CFO)

Quorenta Sweden AB
Rönnvägen 14, SE-175 43 JÄRFÄLLA, Sweden
Mobile: +46701 23 45 67 | Office: +46 8 52 61 74
www.quorenta-example.com

Font styles to use
Sans Serif

```html
<!DOCTYPE html>
<html lang="en">
<head>
<meta charset="utf-8">
<title>Quorenta Business Cards</title>
<link rel="stylesheet" href="https://fonts.googleapis.com/css2?family=Montserrat:wght@800&family=Roboto:wght@300;400;500&display=swap">
<style>
  :root {
    --brand-blue: #1f5b8a;
    --ink-blue: #2a5d8c;
    --text-grey: #3a3a3a;
    --muted: #8a8f96;
    --card-white: #ffffff;
    --stage: #2a2b30;
    --silver: #c9ccd1;
  }
  * { box-sizing: border-box; margin: 0; padding: 0; }
  html, body { width: 1200px; height: 800px; overflow: hidden; }
  body {
    background: var(--stage);
    font-family: "Roboto", Arial, sans-serif;
    display: flex; align-items: center; justify-content: center; gap: 50px;
  }
  .card {
    width: 525px; height: 300px; position: relative;
    box-shadow: 0 18px 40px rgba(0,0,0,.45);
  }
  .card-front {
    background: var(--brand-blue);
    display: flex; align-items: center; justify-content: center;
  }
  .brand {
    display: flex; align-items: center; gap: 14px;
    font-family: "Roboto", Arial, sans-serif; font-weight: 500;
    letter-spacing: 2px;
  }
  .brand-dot { border-radius: 50%; }
  .card-front .brand { color: var(--silver); font-size: 58px; }
  .card-front .brand-dot { width: 42px; height: 42px; background: var(--silver); }

  .card-back { background: var(--card-white); padding: 34px 40px; }
  .card-back .brand { color: var(--ink-blue); font-size: 40px; justify-content: center; }
  .card-back .brand-dot { width: 28px; height: 28px; background: var(--ink-blue); }

  .person { text-align: center; margin-top: 18px; }
  .person-name {
    font-family: "Montserrat", Arial, sans-serif; font-weight: 800;
    color: var(--ink-blue); font-size: 20px; letter-spacing: .5px; text-transform: uppercase;
  }
  .person-title { font-weight: 300; color: var(--text-grey); font-size: 14px; margin-top: 2px; }
  .rule { width: 46px; height: 1px; background: var(--text-grey); margin: 10px auto 0; }

  .details {
    display: flex; justify-content: center; align-items: flex-start;
    gap: 20px; margin-top: 16px; font-size: 12.5px; color: var(--text-grey); line-height: 1.45;
  }
  .address { text-align: right; }
  .divider { width: 1px; height: 56px; background: var(--text-grey); }
  .contacts li { list-style: none; display: flex; align-items: center; gap: 7px; }
  .contacts svg { width: 12px; height: 12px; fill: var(--ink-blue); flex: none; }
  .website { text-align: center; margin-top: 10px; font-size: 12.5px; color: var(--text-grey); }
  .website::before { content: ""; display: block; width: 46px; height: 1px; background: var(--text-grey); margin: 0 auto 6px; }
</style>
</head>
<body>
  <section class="card card-front" aria-label="Card front">
    <div class="brand"><span class="brand-dot"></span>Quorenta</div>
  </section>

  <section class="card card-back" aria-label="Card back">
    <div class="brand"><span class="brand-dot"></span>Quorenta</div>
    <div class="person">
      <p class="person-name">Lotta Berglund</p>
      <p class="person-title">Chief Financial Officer (CFO)</p>
      <div class="rule"></div>
    </div>
    <div class="details">
      <address class="address" style="font-style:normal">
        Quorenta Sweden AB<br>
        Rönnvägen 14, SE-175<br>
        43 JÄRFÄLLA, Sweden
      </address>
      <div class="divider"></div>
      <ul class="contacts">
        <li><svg viewBox="0 0 24 24" aria-hidden="true"><path d="M6.6 10.8a15 15 0 0 0 6.6 6.6l2.2-2.2c.3-.3.7-.4 1-.2 1.1.4 2.3.6 3.6.6.6 0 1 .4 1 1V20c0 .6-.4 1-1 1A17 17 0 0 1 3 4c0-.6.4-1 1-1h3.5c.6 0 1 .4 1 1 0 1.3.2 2.5.6 3.6.1.3 0 .7-.2 1z"/></svg>+46 8 52 61 74</li>
        <li><svg viewBox="0 0 24 24" aria-hidden="true"><path d="M7 1h10a2 2 0 0 1 2 2v18a2 2 0 0 1-2 2H7a2 2 0 0 1-2-2V3a2 2 0 0 1 2-2zm0 3v14h10V4zm5 15.5a1 1 0 1 0 0 2 1 1 0 0 0 0-2z"/></svg>+46701 23 45 67</li>
        <li><svg viewBox="0 0 24 24" aria-hidden="true"><path d="M2 5h20v14H2zm2 2v.5l8 5 8-5V7z"/></svg>l_berglund@quorenta-example.com</li>
      </ul>
    </div>
    <p class="website">www.quorenta-example.com</p>
  </section>
</body>
</html>
```